Refresh of The Marston Collective business card

Update business card design using existing primary logo. Names, numbers, etc. are too hard to read on current design.

Target Market(s)

We are a CPA firm.

Industry/Entity Type

Accountant

Contact Information for Business Card

update current card

Colors
0355a3
3176b5
85acd3
0792cd

Requirements
Must have
• Easier to read phone numbers and names
• Use existing logo
Nice to have
• We love our color scheme and current TMC logo. But the names and phone numbers are too small and card just look old and stale.

```html
<!DOCTYPE html>
<html lang="en">
<head>
<meta charset="utf-8">
<title>The Marston Collective – Business Card</title>
<link rel="stylesheet" href="https://fonts.googleapis.com/css2?family=Montserrat:wght@400;500&family=Oswald:wght@600&display=swap">
<style>
  :root {
    --backdrop: #2a2b2e;
    --navy: #21356b;
    --navy-light: #31497c;
    --ink: #2b2b2f;
    --rule: #55585e;
    --paper: #ffffff;
  }
  html, body {
    margin: 0;
    padding: 0;
    width: 1200px;
    height: 900px;
    overflow: hidden;
    background: var(--backdrop);
  }
  .canvas {
    position: relative;
    width: 1200px;
    height: 900px;
  }
  .card {
    position: absolute;
    left: 290px;
    width: 620px;
    height: 354px;
    box-sizing: border-box;
    overflow: hidden;
    box-shadow: 0 10px 30px rgba(0,0,0,.45);
  }
  .card-front {
    top: 76px;
    background: linear-gradient(135deg, var(--navy) 0%, var(--navy-light) 100%);
    color: var(--paper);
    font-family: "Montserrat", sans-serif;
  }
  .logo-lockup {
    position: absolute;
    left: 118px;
    top: 96px;
    display: flex;
    align-items: center;
    gap: 26px;
  }
  .logo-circle {
    width: 118px;
    height: 118px;
    border-radius: 50%;
    background: var(--paper);
    box-shadow: 0 0 0 3px var(--navy), 0 0 0 6px var(--paper);
    flex: none;
  }
  .logo-text {
    display: flex;
    flex-direction: column;
  }
  .firm-name {
    font-size: 30px;
    font-weight: 500;
    line-height: 1.15;
    letter-spacing: 1px;
    margin: 0;
  }
  .firm-tagline {
    margin-top: 10px;
    font-size: 9.5px;
    font-weight: 500;
    letter-spacing: 3px;
    text-transform: uppercase;
  }
  .website {
    position: absolute;
    left: 0;
    right: 0;
    top: 292px;
    text-align: center;
    font-size: 15px;
    letter-spacing: 1px;
  }
  .card-back {
    top: 470px;
    background: var(--paper);
    color: var(--ink);
    font-family: "Montserrat", sans-serif;
  }
  .identity {
    position: absolute;
    right: 310px;
    top: 112px;
    text-align: right;
  }
  .person-name {
    margin: 0;
    font-family: "Oswald", sans-serif;
    font-weight: 600;
    font-size: 27px;
    line-height: 1.1;
    color: var(--navy);
    white-space: nowrap;
  }
  .person-role {
    margin-top: 4px;
    font-size: 18px;
    color: var(--ink);
  }
  .divider {
    position: absolute;
    left: 330px;
    top: 100px;
    width: 2px;
    height: 100px;
    background: var(--rule);
  }
  .contact-list {
    position: absolute;
    left: 348px;
    top: 100px;
    margin: 0;
    padding: 0;
    list-style: none;
    font-size: 16px;
    line-height: 25px;
    white-space: nowrap;
  }
  .contact-list li {
    display: flex;
    align-items: center;
    gap: 12px;
  }
  .contact-list svg {
    width: 14px;
    height: 14px;
    fill: var(--navy);
    flex: none;
  }
  .address {
    position: absolute;
    left: 0;
    right: 0;
    top: 272px;
    text-align: center;
    font-size: 17px;
    letter-spacing: .5px;
  }
</style>
</head>
<body>
<main class="canvas">
  <section class="card card-front">
    <div class="logo-lockup">
      <div class="logo-circle"></div>
      <div class="logo-text">
        <p class="firm-name">The Marston<br>Collective</p>
        <span class="firm-tagline">Certified Public Accountants</span>
      </div>
    </div>
    <div class="website">www.marstoncollective.com</div>
  </section>

  <section class="card card-back">
    <div class="identity">
      <h1 class="person-name">DANIEL R. MARSTON, CPA</h1>
      <div class="person-role">Founder</div>
    </div>
    <div class="divider"></div>
    <ul class="contact-list">
      <li>
        <svg viewBox="0 0 16 16" aria-hidden="true"><path d="M3.5 1l2.5 3-1.5 1.6c.9 2 2.4 3.5 4.4 4.4L10.5 8.5l3 2.5-1.2 2.6c-.3.5-.8.6-1.3.5C6.4 12.9 3.1 9.6 1.9 5c-.1-.5 0-1 .5-1.3z"/></svg>
        <span>555.214.3087</span>
      </li>
      <li>
        <svg viewBox="0 0 16 16" aria-hidden="true"><path d="M4.5 0h7a1 1 0 0 1 1 1v14a1 1 0 0 1-1 1h-7a1 1 0 0 1-1-1V1a1 1 0 0 1 1-1zm.8 2v10.5h5.4V2zM8 13.3a.9.9 0 1 0 0 1.8.9.9 0 0 0 0-1.8z"/></svg>
        <span>555.362.9140</span>
      </li>
      <li>
        <svg viewBox="0 0 16 16" aria-hidden="true"><path d="M4 1h8v4H4zM1.5 6h13a1 1 0 0 1 1 1v5h-3v3h-9v-3h-3V7a1 1 0 0 1 1-1zm3.5 5v3h6v-3z"/></svg>
        <span>555.481.7725</span>
      </li>
      <li>
        <svg viewBox="0 0 16 16" aria-hidden="true"><path d="M0 3h16v1.2L8 9 0 4.2zM0 5.8l8 4.8 8-4.8V13H0z"/></svg>
        <span>dan@marstoncollective.com</span>
      </li>
    </ul>
    <div class="address">318 Alder Creek Rd. Suite 104 Brookhaven, Ohio 45210</div>
  </section>
</main>
</body>
</html>
```